Zarvo! Next Steps?, Bail Bond Company Check-in App , Court date, Court Reminders, Payments

Zarvo!
Next Steps?
WINNER OF THIS CONTEST WILL HAVE OPPORTUNITY TO DESIGN CUSTOMIZE SOME OUR COMPANY PAGES AFTER CONTEST!
Check-in with your Bail agent via pic/video
Receive Court reminders
Make a payments

Basically this app is a portal to 3rd party bail companies.
The idea is for the person whom makes bail downloads the Zarvo app from App Store.
Then they select a bail bond company.
This would be similar to a restaurant, real estate agent, insurance agent,,app where we could populate bail bond companies by client location or by typing in name of bail company.
We would like the ability to customize each bail bond company landing pages but are open to a global concept. when you click the bail bond company location it would have the logos for that company so the bail bond company screens would need to be customizeble
The app will require a photo or video check-in that is date and time
stamped with a gps location stored in check-in history
Check-in can be scheduled or random or voluntary
Voluntary and Scheduled Check-ins would require check-in button
Random would be via alert or text

The app should be able to receive court date updates
The app should allow clients to make payments to bail bond company
we need
ZARVO! landing page
client registration screens, check-in screens, available bail bond company screens for client to choose from
client registration page should include
name
email address
phone number
picture
home address
work address
date of birth
this app is different from our u-trak app. this is a bail bond check-in app for third party bail bond companies.
landing page should be ZARVO! Next Steps?
ZARVO ! Registration
Find your bail bond Company should list bail bond companies near me and search bar for searching bail bond companies by name
Next landing pages would be customizable for the third party bail bond companies
these would include pages for
check-ins via pics/videos
payment page
court reminders
contact information for bail bond companies
Zarvo Pages include
initial landing page
registration page
search bail companies

Bail bond company pages should include
Bali bond company landing page
Use KELNOR BAIL BOND COMPANY as example
contact information for bail company
check-in page
payment page
court reminder page
Updates

Low designer entries

Low designer entries

Sick

Sick

Sick

Target Market(s)

Court Defendants, Probation ,jails, sheriffs, judges, attorneys

Industry/Entity Type

justice, law enforcement, courts,

Requirements
Must have
• Check-in via pic/video, ability to receive court date reminders, make paymentswe need client registration screens, check-in screens, available bail bond company screens for client to choose from
Nice to have
• Professional easy to navigate intuitive customizable to 3rd party bail bond companies, logos,phone numbers etc.
Should not have
• unprofessional graphics,

```html
<!DOCTYPE html>
<html lang="en">
<head>
<meta charset="utf-8">
<title>Registration – Zarvo</title>
<link href="https://fonts.googleapis.com/css2?family=Playfair+Display:wght@900&family=Poppins:wght@400;600;700&display=swap" rel="stylesheet">
<style>
  :root {
    --bg: #ffffff;
    --ink: #141414;
    --muted: #5a5a5a;
    --placeholder: #7a7a7a;
    --field: #eeeeee;
    --dash: #c4c4c4;
    --brand-red: #be1e2d;
    --white: #ffffff;
  }
  * { box-sizing: border-box; margin: 0; padding: 0; }
  html, body {
    width: 1200px; height: 2594px; overflow: hidden;
    background: var(--bg);
    font-family: "Poppins", sans-serif;
    color: var(--ink);
  }
  .screen { position: relative; width: 1200px; height: 2594px; }
  .page-title {
    position: absolute; top: 218px; left: 0; width: 100%;
    text-align: center;
    font-family: "Playfair Display", serif; font-weight: 900;
    font-size: 112px; line-height: 140px; letter-spacing: -0.5px;
  }
  .page-subtitle {
    position: absolute; top: 370px; left: 0; width: 100%;
    text-align: center; font-size: 36px; line-height: 50px; color: var(--muted);
  }
  .field-label {
    position: absolute; left: 103px;
    font-weight: 700; font-size: 26px; line-height: 36px; letter-spacing: 0.3px;
  }
  .field-input {
    position: absolute; left: 103px; width: 1006px; height: 115px;
    background: var(--field); border-radius: 10px;
    display: flex; align-items: center; padding: 0 45px;
    font-size: 27px; color: var(--placeholder);
  }
  .field-input .calendar-icon { margin-left: auto; width: 40px; height: 40px; }
  .upload-box {
    position: absolute; left: 103px; top: 1108px; width: 1006px; height: 411px;
    background: var(--field); border-radius: 10px;
  }
  .upload-area {
    position: absolute; inset: 28px;
    border: 3px dashed var(--dash); border-radius: 10px;
    display: flex; align-items: center; justify-content: center;
  }
  .upload-icon {
    width: 155px; height: 155px; border-radius: 50%; background: var(--white);
    display: flex; align-items: center; justify-content: center;
  }
  .submit-button {
    position: absolute; left: 103px; top: 2224px; width: 1006px; height: 141px;
    background: var(--brand-red); border-radius: 10px; border: none;
    color: var(--white); font-family: "Poppins", sans-serif; font-weight: 700;
    font-size: 46px; letter-spacing: 0.5px;
    display: flex; align-items: center; justify-content: center;
  }
  .submit-button svg { position: absolute; right: 48px; top: 50%; transform: translateY(-50%); }
</style>
</head>
<body>
<main class="screen">
  <h1 class="page-title">Registration</h1>
  <p class="page-subtitle">Online Zarvo App</p>

  <label class="field-label" style="top:478px">NAME*</label>
  <div class="field-input" style="top:526px">Enter name</div>

  <label class="field-label" style="top:667px">EMAIL ADDRESS*</label>
  <div class="field-input" style="top:714px">Enter email address</div>

  <label class="field-label" style="top:861px">PHONE NUMBER*</label>
  <div class="field-input" style="top:908px">Enter phone number</div>

  <label class="field-label" style="top:1054px">PICTURE*</label>
  <div class="upload-box">
    <div class="upload-area">
      <div class="upload-icon">
        <svg width="66" height="62" viewBox="0 0 33 31" fill="none" stroke="#141414" stroke-width="2" stroke-linecap="round" stroke-linejoin="round">
          <path d="M24 13V4a2 2 0 0 0-2-2H4a2 2 0 0 0-2 2v20a2 2 0 0 0 2 2h15"/>
          <circle cx="9" cy="9" r="2.5"/>
          <path d="M2 22l7-7 5 5 3-3 5 5"/>
          <path d="M27 29V18M23 22l4-4 4 4"/>
        </svg>
      </div>
    </div>
  </div>

  <label class="field-label" style="top:1568px">HOME ADDRESS*</label>
  <div class="field-input" style="top:1615px">Enter home address</div>

  <label class="field-label" style="top:1762px">WORK ADDRESS*</label>
  <div class="field-input" style="top:1809px">Enter work address</div>

  <label class="field-label" style="top:1955px">DATE OF BIRTH *</label>
  <div class="field-input" style="top:2003px">Select date of birth
    <svg class="calendar-icon" viewBox="0 0 20 20" fill="none" stroke="#141414" stroke-width="1.3">
      <rect x="2" y="3.5" width="16" height="14.5" rx="1.5"/>
      <path d="M6 2v3M14 2v3M2 7h16"/>
      <g fill="#141414" stroke="none">
        <rect x="5" y="9" width="2" height="2"/><rect x="9" y="9" width="2" height="2"/><rect x="13" y="9" width="2" height="2"/>
        <rect x="5" y="12.5" width="2" height="2"/><rect x="9" y="12.5" width="2" height="2"/><rect x="13" y="12.5" width="2" height="2"/>
      </g>
    </svg>
  </div>

  <button class="submit-button">SUBMIT
    <svg width="50" height="46" viewBox="0 0 25 23" fill="#ffffff">
      <path d="M24 1L1 10l7 3 2 9 4-6 6 4z M8 13l12-9-9 11z" fill-rule="evenodd"/>
    </svg>
  </button>
</main>
</body>
</html>
```